Website design for a construction company

The logo and the copies of all the 3 pages are attached below. I don't have a preference in colors but I would ideally like to use the colors on my logo, dark teal (secondary) and copper (primary).

Company Name: Vostrane Group

Location: London, UK

Business Overview:

Vostrane Group is a comprehensive construction company based in London, specializing in a wide range of construction services. We cater to various sectors, providing services including electrical work, painting and decorating, plastering, plumbing, carpentry, kitchen and bathroom installations, loft conversions, and extensions. Our team is known for its skilled craftsmanship, attention to detail, and commitment to quality.

What "VOSTRANE" stands for:

Our company name, 'VOSTRANE', is derived from Vostranion, the ancient Greek god of craftsmen, blacksmiths, artisans, sculptors, metals, metallurgy, fire, and volcanoes. Vostranion was renowned in mythology for his incredible skill in crafting and creating, making him the patron of all craftsmen and artisans. His name is synonymous with the mastery of artisanship and the creation of wondrous, enduring works.

In choosing 'VOSTRANE' as our name, we embody the spirit and skills of Vostranion. It reflects our commitment to craftsmanship, excellence, and durability in the field of construction. Just as Vostranion was known for his meticulous work, precision, and innovative creations, our company strives to uphold these qualities in every project we undertake.

Our name is a constant reminder of our dedication to quality, innovation, and the art of building. It symbolizes our endeavor to achieve the highest standards in construction, much like Vostranion did in his timeless creations. In essence, 'VOSTRANE' is not just our name; it's a representation of our ethos and the high standards we set for ourselves in the construction industry.

Target Audience:

Our primary audience includes homeowners, real estate developers, and commercial clients in London seeking reliable, high-quality construction services.

Unique Selling Points:

Diverse Range of Services: Offering a one-stop solution for all construction needs.

Certified and Experienced: Professional team with a strong focus on delivering certified and compliant work, particularly in electrical services.

Client-Centric Approach: Emphasizing client satisfaction, we tailor our services to meet the unique needs and visions of our clients.

Quality and Reliability: Commitment to high-quality materials, skilled workmanship, and delivering projects on time and within budget.

Website Requirements:

Clean, professional design reflecting the quality and reliability of our services.

User-friendly navigation to easily access information about our services, portfolio, company background, and contact details.

Portfolio section showcasing our past projects with placeholders for images and descriptions.

Integration of a contact form, map for our location, and links to our social media accounts.

Mobile-responsive design to ensure accessibility across various devices.

Purpose of the Website:
The website aims to:

Establish an online presence and credibility in the construction industry.

Provide an informative resource about our services and past projects to potential clients.

Facilitate easy communication and inquiries through an integrated contact system.

Tone and Style:

Professional, informative, and welcoming. The website should convey trustworthiness and expertise in the construction field.

Target Market(s)

homeowners, real estate developers, and commercial clients

Industry/Entity Type

Construction

Number of Pages Required

3 page

Colors

Designer to choose colors to be used in the design.

```html
<!DOCTYPE html>
<html lang="en">
<head>
<meta charset="utf-8">
<title>Vostrane Group — Construction in London</title>
<link href="https://fonts.googleapis.com/css2?family=Poppins:wght@400;500;600&family=Oswald:wght@400;500&display=swap" rel="stylesheet">
<style>
:root{
  --copper:#b0843f;
  --teal:#17918a;
  --ink:#1c1c1c;
  --text:#3a3a3a;
  --soft:#f3f3f3;
  --footer:#1b1b1b;
  --line:#e6d7c1;
}
*{box-sizing:border-box;margin:0;padding:0}
html,body{width:1200px;height:3731px;overflow:hidden}
body{position:relative;font-family:'Poppins',sans-serif;color:var(--ink);background:#fff}
.btn{position:absolute;background:var(--copper);color:#fff;font-size:13px;font-weight:500;display:flex;align-items:center;justify-content:center;border-radius:4px}
.brand{display:flex;align-items:center;gap:10px;color:var(--ink);font-weight:500;letter-spacing:1px;white-space:nowrap}
.brand .mark{width:26px;height:26px;background:var(--teal);flex:none}

/* header */
.site-header{position:absolute;left:0;top:0;width:1200px;height:70px;background:#fff}
.site-header .brand{position:absolute;left:145px;top:21px;font-size:20px}
.nav{position:absolute;left:635px;top:27px;display:flex;gap:29px;font-size:13px;font-weight:500}
.nav .active{color:var(--teal)}
.site-header .btn{left:949px;top:19px;width:110px;height:33px}

/* hero */
.hero{position:absolute;left:0;top:70px;width:1200px;height:474px;background:linear-gradient(90deg,#3d3530 0%,#6a5c4f 45%,#b7a894 75%,#d8d2c8 100%)}
.hero h1{position:absolute;left:141px;top:144px;font-size:47px;line-height:60px;font-weight:600;color:#fff}
.hero p{position:absolute;left:141px;top:283px;width:400px;font-size:14px;line-height:25px;color:#fff}
.hero .btn{left:141px;top:359px;width:110px;height:32px}

/* about */
.about-photo{position:absolute}
.about h2{position:absolute;left:656px;top:656px;font-size:27px;font-weight:600}
.about h2 span,.services h2 span{color:var(--copper)}
.about .rule{position:absolute;left:656px;top:696px;width:84px;height:2px;background:var(--teal)}
.about p{position:absolute;left:656px;top:722px;width:392px;font-size:12.5px;line-height:22.5px;color:var(--text)}
.about .btn{left:656px;top:856px;width:110px;height:32px}

/* services */
.services h2{position:absolute;left:0;width:1200px;top:1028px;text-align:center;font-size:27px;font-weight:600}
.services .rule{position:absolute;left:557px;top:1069px;width:86px;height:2px;background:var(--teal)}
.services p{position:absolute;left:290px;top:1092px;width:620px;text-align:center;font-size:12.5px;line-height:23px;color:var(--text)}
.card{position:absolute;width:214px;height:171px;border:1.5px solid var(--line);border-radius:8px;background:#fff;text-align:center}
.card .icon{position:absolute;left:72px;top:24px;width:70px;height:70px;border-radius:50%;background:var(--copper);display:flex;align-items:center;justify-content:center}
.card .name{position:absolute;left:10px;right:10px;top:112px;font-size:15.5px;line-height:24px;font-weight:500}
.card.active{background:var(--copper);border-color:var(--copper)}
.card.active .icon{background:#fff}
.card.active .name{color:#f4e8d6}

/* testimonials */
.reviews{position:absolute;left:0;top:1620px;width:1200px;height:535px;background:var(--soft)}
.heading-cond{font-family:'Oswald',sans-serif;font-weight:400}
.heading-cond b{font-weight:500}
.reviews h2{position:absolute;left:0;width:1200px;top:80px;text-align:center;font-size:34px}
.reviews .lead{position:absolute;left:210px;width:780px;top:131px;text-align:center;font-size:12.5px;line-height:22px;color:var(--text)}
.review{position:absolute;top:220px;width:448px;height:225px;background:#fff;border-radius:8px;box-shadow:0 2px 10px rgba(0,0,0,.12);text-align:center}
.review .top{position:absolute;left:63px;top:-3px;width:322px;height:2px;background:var(--copper)}
.review .bottom{position:absolute;left:63px;bottom:-3px;width:322px;height:3px;background:var(--teal)}
.review .quote{position:absolute;left:202px;top:-25px;width:44px;height:44px;border-radius:50%;background:var(--copper);color:#fff;font-family:Georgia,serif;font-size:38px;line-height:56px}
.review h3{position:absolute;left:0;right:0;top:33px;font-size:14px;font-weight:600}
.review .stars{position:absolute;left:0;right:0;top:56px;display:flex;justify-content:center}
.review p{position:absolute;left:16px;right:16px;top:87px;font-size:12.5px;line-height:22px;color:var(--text)}
.arrow{position:absolute;top:300px;width:70px;height:70px;border-radius:50%;display:flex;align-items:center;justify-content:center}
.arrow.prev{left:55px;border:1.5px solid var(--ink);background:#fff}
.arrow.next{left:1075px;background:var(--teal)}

/* inquiry */
.inquiry{position:absolute;left:206px;top:2249px;width:787px;height:569px;background:var(--teal);border-radius:14px}
.inquiry h2{position:absolute;left:0;right:0;top:62px;text-align:center;color:#fff;font-size:34px}
.field{position:absolute;width:312px}
.field label{display:block;font-size:9px;color:#fff;margin-bottom:6px}
.field .box{height:47px;border:1.5px solid #fff;border-radius:2px;color:#fff;font-size:12.5px;padding:14px 18px}
.field.wide{width:664px}
.field.wide .box{height:142px}
.inquiry .submit{position:absolute;left:323px;top:469px;width:142px;height:41px;background:#fff;color:var(--copper);border:1px solid var(--copper);font-size:13px;display:flex;align-items:center;justify-content:center}

/* cta */
.cta h2{position:absolute;left:0;width:1200px;top:2893px;text-align:center;font-size:34px}
.cta p{position:absolute;left:0;width:1200px;top:2955px;text-align:center;font-size:12.5px;color:var(--text)}
.cta .btn{left:535px;top:2996px;width:142px;height:41px;border-radius:0}

/* footer */
.site-footer{position:absolute;left:0;top:3123px;width:1200px;height:282px;background:var(--footer);color:#fff}
.site-footer h4{position:absolute;font-family:'Oswald',sans-serif;font-weight:500;font-size:15px}
.links{position:absolute;left:142px;top:102px;list-style:none;font-size:12.5px;line-height:34.6px}
.site-footer .brand{position:absolute;left:0;width:1200px;justify-content:center;top:128px;color:#fff;font-size:46px;font-weight:400;gap:14px}
.site-footer .brand .mark{width:44px;height:44px}
.socials{position:absolute;left:532px;top:222px;display:flex;gap:6px}
.socials span{width:29px;height:29px;border:1.5px solid #fff;border-radius:50%}
.contact{position:absolute;left:884px;font-size:12.5px;line-height:22px;display:flex;gap:8px;align-items:flex-start}
</style>
</head>
<body>

<header class="site-header">
  <div class="brand"><span class="mark"></span>VOSTRANE GROUP</div>
  <nav class="nav"><span class="active">Home</span><span>About Us</span><span>Services</span><span>Projects</span></nav>
  <div class="btn">Contact Us</div>
</header>

<section class="hero" role="img" aria-label="Photo of an engineer and a site worker in hard hats reviewing plans in front of a building under construction">
  <h1>Building Your<br>Dreams Into Reality</h1>
  <p>Expert Craftsmanship Meets Unmatched Reliability in the Heart of London</p>
  <div class="btn">Learn More</div>
</section>

<section class="about">
  <div class="about-photo" style="left:141px;top:678px;width:208px;height:264px;background:linear-gradient(160deg,#c9d2da,#8a7a6a 60%,#c8773a)" role="img" aria-label="Photo of a smiling site worker and a businessman near a crane"></div>
  <div class="about-photo" style="left:367px;top:627px;width:208px;height:274px;background:linear-gradient(160deg,#a98b6b,#6f5f52 55%,#c9b89c)" role="img" aria-label="Photo of two workers in hard hats checking drawings on site"></div>
  <h2>About <span>Vostrane</span> Group</h2>
  <div class="rule"></div>
  <p>Where Construction Meets Excellence. Based in London, we are committed to transforming your spaces into exceptional places. Our team is dedicated to delivering the highest quality in every project, attending to every detail with precision and care.</p>
  <div class="btn">Learn More</div>
</section>

<section class="services">
  <h2>Our <span>Services</span></h2>
  <div class="rule"></div>
  <p>Tailored to Your Needs. Discover how we can bring your vision to life, covering every aspect of construction from the initial design to the final touches.</p>

  <div class="card" style="left:141px;top:1180px"><div class="icon"><svg width="32" height="32" viewBox="0 0 32 32"><path d="M18 3 8 18h7l-2 11 11-16h-7z" fill="none" stroke="#fff" stroke-width="2" stroke-linejoin="round"/></svg></div><div class="name">Electrical Work</div></div>
  <div class="card active" style="left:375px;top:1180px"><div class="icon"><svg width="32" height="32" viewBox="0 0 32 32"><rect x="6" y="4" width="20" height="9" rx="2" fill="none" stroke="#b0843f" stroke-width="2"/><path d="M16 13v6M13 19h6v10h-6z" fill="none" stroke="#b0843f" stroke-width="2"/></svg></div><div class="name">Painting and<br>Decorating</div></div>
  <div class="card" style="left:609px;top:1180px"><div class="icon"><svg width="32" height="32" viewBox="0 0 32 32"><path d="M6 8h20l-4 8H10z M16 16v12" fill="none" stroke="#fff" stroke-width="2" stroke-linejoin="round"/></svg></div><div class="name">Plastering</div></div>
  <div class="card" style="left:843px;top:1180px"><div class="icon"><svg width="32" height="32" viewBox="0 0 32 32"><path d="M4 10h16v6H4zM20 12h6v14M10 16v6" fill="none" stroke="#fff" stroke-width="2"/></svg></div><div class="name">Plumbing</div></div>

  <div class="card" style="left:141px;top:1372px"><div class="icon"><svg width="32" height="32" viewBox="0 0 32 32"><path d="M6 26 22 10M18 6l8 8M8 8l16 16" fill="none" stroke="#fff" stroke-width="2" stroke-linecap="round"/></svg></div><div class="name">Carpentry</div></div>
  <div class="card" style="left:375px;top:1372px"><div class="icon"><svg width="32" height="32" viewBox="0 0 32 32"><rect x="5" y="12" width="22" height="14" rx="1" fill="none" stroke="#fff" stroke-width="2"/><path d="M5 18h22M12 12V7h8v5" fill="none" stroke="#fff" stroke-width="2"/></svg></div><div class="name">Kitchen and Bathroom<br>Installations</div></div>
  <div class="card" style="left:609px;top:1372px"><div class="icon"><svg width="32" height="32" viewBox="0 0 32 32"><path d="M5 6h22l-8 10v10l-6-3v-7z" fill="none" stroke="#fff" stroke-width="2" stroke-linejoin="round"/></svg></div><div class="name">Loft Conversions</div></div>
  <div class="card" style="left:843px;top:1372px"><div class="icon"><svg width="32" height="32" viewBox="0 0 32 32"><g fill="none" stroke="#fff" stroke-width="2"><rect x="5" y="5" width="9" height="9"/><rect x="5" y="18" width="9" height="9"/><rect x="18" y="18" width="9" height="9"/><path d="M22.5 3l5 5-5 5-5-5z"/></g></svg></div><div class="name">Extensions</div></div>
</section>

<section class="reviews">
  <h2 class="heading-cond"><b>Hear from</b> Our Satisfied Clients</h2>
  <p class="lead">Our commitment to excellence has earned us the trust of numerous homeowners and businesses in London. Read their stories and understand the Vostrane Group difference.</p>

  <article class="review" style="left:141px">
    <div class="top"></div><div class="quote">“</div>
    <h3>Martin Hale</h3>
    <div class="stars"><svg width="102" height="14" viewBox="0 0 102 14"><g fill="#f2b600"><path id="st" d="M7 0l2 4.5 5 .5-3.8 3.2 1.2 5L7 10.6 2.6 13.2l1.2-5L0 5l5-.5z"/><use href="#st" x="22"/><use href="#st" x="44"/><use href="#st" x="66"/><use href="#st" x="88"/></g></svg></div>
    <p>"Lorem ipsum dolor sit amet, consectetur adipiscing elit, sed do eiusmod tempor incididunt ut labore et dolore magna aliqua. Ut enim ad minim veniam, quis nostrud exercitation ullamco laboris nisi ut aliquip ex ea commodo consequat."</p>
    <div class="bottom"></div>
  </article>
  <article class="review" style="left:610px">
    <div class="top"></div><div class="quote">“</div>
    <h3>Clara Reed</h3>
    <div class="stars"><svg width="102" height="14" viewBox="0 0 102 14"><g fill="#f2b600"><use href="#st"/><use href="#st" x="22"/><use href="#st" x="44"/><use href="#st" x="66"/><use href="#st" x="88"/></g></svg></div>
    <p>"Lorem ipsum dolor sit amet, consectetur adipiscing elit, sed do eiusmod tempor incididunt ut labore et dolore magna aliqua. Ut enim ad minim veniam, quis nostrud exercitation ullamco laboris nisi ut aliquip ex ea commodo consequat."</p>
    <div class="bottom"></div>
  </article>

  <div class="arrow prev"><svg width="28" height="16" viewBox="0 0 28 16"><path d="M27 8H2M8 2 2 8l6 6" fill="none" stroke="#1c1c1c" stroke-width="2"/></svg></div>
  <div class="arrow next"><svg width="28" height="16" viewBox="0 0 28 16"><path d="M1 8h25M20 2l6 6-6 6" fill="none" stroke="#fff" stroke-width="2"/></svg></div>
</section>

<section class="inquiry">
  <h2 class="heading-cond"><b>Quick</b> Inquiry</h2>
  <div class="field" style="left:62px;top:116px"><label>First Name*</label><div class="box">First Name</div></div>
  <div class="field" style="left:414px;top:116px"><label>Last Name*</label><div class="box">Last Name</div></div>
  <div class="field" style="left:62px;top:206px"><label>Email Address*</label><div class="box">Email Address</div></div>
  <div class="field" style="left:414px;top:206px"><label>Phone Number*</label><div class="box">Phone Number</div></div>
  <div class="field wide" style="left:62px;top:296px"><label>Email Address*</label><div class="box">Email Address</div></div>
  <div class="submit">Submit Now</div>
</section>

<section class="cta">
  <h2 class="heading-cond"><b>Ready</b> to Start Your Project?</h2>
  <p>Contact us today for a consultation and embark on the journey to turn your construction dreams into a stunning reality.</p>
  <div class="btn">Contact Us</div>
</section>

<footer class="site-footer">
  <h4 style="left:142px;top:57px">Quick Links</h4>
  <ul class="links"><li>Home</li><li>About Us</li><li>Services</li><li>Projects</li><li>Contact Us</li></ul>
  <div class="brand"><span class="mark"></span>VOSTRANE</div>
  <div class="socials"><span></span><span></span><span></span><span></span></div>
  <h4 style="left:884px;top:57px">Contact Details</h4>
  <div class="contact" style="top:102px"><svg width="14" height="20" viewBox="0 0 14 20"><path d="M7 0a7 7 0 0 0-7 7c0 5 7 13 7 13s7-8 7-13a7 7 0 0 0-7-7zm0 10a3 3 0 1 1 0-6 3 3 0 0 1 0 6z" fill="#fff"/></svg><span>123, Building Name,<br>Lorem Street, UK 123456</span></div>
  <div class="contact" style="top:180px"><svg width="20" height="20" viewBox="0 0 20 20"><path d="M4 1l4 4-2 3c1 2 3 4 5 5l3-2 4 4-3 3C8 18 2 12 1 4z" fill="none" stroke="#fff" stroke-width="1.6"/></svg><span>123-456-7890</span></div>
  <div class="contact" style="top:238px"><svg width="22" height="16" viewBox="0 0 22 16"><rect x="1" y="1" width="20" height="14" fill="none" stroke="#fff" stroke-width="1.6"/><path d="M1 1l10 8 10-8" fill="none" stroke="#fff" stroke-width="1.6"/></svg><span>info@vostrane.com</span></div>
</footer>

</body>
</html>
```